DinA5 Flyer für italienischen Tuning-Shop
Aufgabenstellung
Wir benötigen einen Flyer im DinA5-Format, eventuell beidseitig. Eine Seite zur ersten Beurteilung würde uns erst mal reichen.
Es dürfen alle unsere Logos verwendet werden. Auch dürfen Fahrzeuge der Marke Vesta Corlano, Nuro und Bravina verwendet werden (sofern ihr da freiverfügbare findet!). Ihr dürft auch die Markennamen nutzen (Nuro, Vesta Corlano, Bravina, Montessa). Es muss ein Plauderbuch-Button drauf sein. Der Text steht noch nicht fest - ihr dürft aber fürs erste Layout gerne selbst derweil einen nehmen. Es dürfen auch Begriffe wie "Luftfilter, Auspuff, Spoiler, etc" fallen. Unsere Adresse etc muss mit drauf sein.

```html
<!DOCTYPE html>
<html lang="de">
<head>
<meta charset="utf-8">
<title>Nuro Welt – Flyer Rückseite</title>
<link rel="stylesheet" href="https://fonts.googleapis.com/css2?family=Jost:wght@300;400&display=swap">
<style>
  :root {
    --green: #2a8a3a;
    --red: #a1232a;
    --ink: #141414;
    --white: #ffffff;
    --blush: #f4cfcf;
    --rose: #e8b3b3;
    --sage: #acc8b1;
  }
  * { margin: 0; padding: 0; box-sizing: border-box; }
  html, body { width: 846px; height: 1200px; overflow: hidden; }
  body {
    font-family: "Jost", "Futura", sans-serif;
    font-weight: 300;
    position: relative;
    background:
      linear-gradient(150deg, var(--white) 0%, var(--white) 30%, var(--blush) 55%, var(--rose) 72%, rgba(232,179,179,0) 80%),
      linear-gradient(155deg, var(--white) 0%, var(--rose) 65%, var(--sage) 88%, var(--sage) 100%);
  }
  .flyer { position: absolute; inset: 0; }
  .contact-heading {
    position: absolute; left: 68px; top: 66px;
    font-size: 43px; color: var(--green); letter-spacing: 1px;
  }
  .address {
    position: absolute; left: 68px; top: 140px;
    font-size: 38px; line-height: 48.5px; color: var(--ink); letter-spacing: 1.5px;
    font-style: normal;
  }
  .channels {
    position: absolute; left: 68px; top: 314px;
    display: grid; grid-template-columns: 156px auto; row-gap: 0;
  }
  .channel-label {
    font-size: 32px; line-height: 48.5px; color: var(--red); letter-spacing: 1px;
    display: flex; align-items: center; gap: 8px;
  }
  .channel-label.social { font-size: 22px; }
  .social-square { width: 14px; height: 14px; background: var(--red); flex: none; }
  .channel-value {
    font-size: 40px; line-height: 48.5px; color: var(--ink); letter-spacing: 1.5px;
  }
  .services {
    position: absolute; left: 0; right: 0; top: 618px;
    text-align: center; list-style: none;
    font-size: 60px; line-height: 72px; color: var(--red); letter-spacing: 1px;
  }
  .services .more { color: var(--green); font-size: 50px; letter-spacing: 3px; }
</style>
</head>
<body>
  <main class="flyer">
    <h2 class="contact-heading">Kontakt:</h2>
    <address class="address">
      Marco Lindenhuber<br>
      Wiesenweg 27<br>
      D-93199 Talheim
    </address>
    <div class="channels">
      <span class="channel-label">tel.:</span><span class="channel-value">09471 - 55210 - 18</span>
      <span class="channel-label">fax:</span><span class="channel-value">09471 - 55210 - 19</span>
      <span class="channel-label">mail:</span><span class="channel-value">shop@nuro-welt.de</span>
      <span class="channel-label social"><span class="social-square"></span>Plauderbuch</span><span class="channel-value">www.plauderbuch.de/NuroWelt</span>
    </div>
    <ul class="services">
      <li>Achsen</li>
      <li>Beleuchtung</li>
      <li>Flügeltüren</li>
      <li>Getriebe</li>
      <li>Elektronik</li>
      <li>HiFi</li>
      <li class="more">... und mehr ...</li>
    </ul>
  </main>
</body>
</html>
```